Business Card Design

I am selling Cruelty Free/not tested on animal products.
Ideally I would like pictures of rabbits/guinea pigs/Beagle(dog)/rat/mice, as these are the main creatures that are tested on.
Background of card Earth, clouds or rainbow.
Yes I am an animal activist.
My favorite colours are purple and green.

Reason: havent got the perfect design as yet

Industry/Entity Type

Business

Contact Information for Business Card

GENTLY BY NATURE
Cruelty Free Products
Norma Faldt
0492 837 514

```html
<!DOCTYPE html>
<html lang="en">
<head>
<meta charset="utf-8">
<title>Gently By Nature – Business Card</title>
<link rel="stylesheet" href="https://fonts.googleapis.com/css2?family=Old+Standard+TT&family=Pinyon+Script&display=swap">
<style>
  :root {
    --stage: #e9e9ec;
    --card: #ffffff;
    --ink: #141414;
    --lilac: #8a6bbd;
    --lilac-soft: #c7b4e6;
    --wash-violet: #d9cbef;
    --wash-green: #d8edc6;
    --splash-warm: #f2a65a;
    --splash-cool: #8fb4e4;
    --fur-brown: #a8642a;
    --fur-cream: #f1ebe3;
    --dog-tan: #b26a33;
  }
  * { box-sizing: border-box; margin: 0; padding: 0; }
  html, body { width: 1200px; height: 1000px; overflow: hidden; }
  body { background: var(--stage); position: relative; }

  .business-card {
    position: absolute; left: 100px; top: 215px;
    width: 1000px; height: 570px;
    background: var(--card);
    border-radius: 26px;
    overflow: hidden;
    box-shadow: 0 8px 24px rgba(0,0,0,0.18);
  }
  .cloud-wash {
    position: absolute; inset: 0;
    background: linear-gradient(160deg, var(--wash-violet) 0%, #ffffff 45%, #ffffff 55%, var(--wash-green) 100%);
  }
  .info-frame {
    position: absolute; left: 128px; top: 82px;
    width: 750px; height: 407px;
    background: var(--card);
    border: 9px solid var(--lilac-soft);
    outline: 2px solid var(--lilac);
    box-shadow: inset 0 0 18px rgba(138,107,189,0.55), 4px 6px 12px rgba(0,0,0,0.25);
  }
  .brand-name {
    position: absolute; left: 270px; top: 140px; width: 610px;
    text-align: center;
    font-family: "Old Standard TT", "Times New Roman", serif;
    font-weight: 400;
    font-size: 48px; letter-spacing: 0.5px; color: var(--ink);
  }
  .tagline {
    position: absolute; left: 270px; top: 210px; width: 610px;
    text-align: center;
    font-family: "Pinyon Script", cursive;
    font-weight: 400;
    font-size: 54px; color: var(--ink);
  }
  .contact-name {
    position: absolute; left: 445px; top: 340px;
    font-family: "Pinyon Script", cursive;
    font-size: 44px; color: var(--ink);
  }
  .contact-phone {
    position: absolute; left: 445px; top: 405px;
    font-family: "Pinyon Script", cursive;
    font-size: 36px; color: var(--ink);
  }
  .rainbow-splash {
    position: absolute; left: 145px; top: 315px;
    width: 290px; height: 120px; border-radius: 40px;
    background: linear-gradient(100deg, var(--splash-warm), var(--splash-cool));
  }
  .guinea-pig-art {
    position: absolute; left: 27px; top: 12px;
    width: 257px; height: 235px; border-radius: 48% 52% 45% 50%;
    background: radial-gradient(ellipse at 65% 60%, var(--fur-cream) 30%, var(--fur-brown) 75%);
    box-shadow: 4px 8px 10px rgba(0,0,0,0.25);
  }
  .beagle-art {
    position: absolute; left: 720px; top: 315px;
    width: 255px; height: 217px; border-radius: 40% 45% 20% 20%;
    background: radial-gradient(ellipse at 45% 55%, #f3eee6 25%, var(--dog-tan) 60%, #2b2420 95%);
    box-shadow: 4px 8px 10px rgba(0,0,0,0.25);
  }
</style>
</head>
<body>
  <div class="business-card">
    <div class="cloud-wash" role="img" aria-label="Purple and green watercolour cloud background"></div>
    <div class="info-frame"></div>
    <div class="rainbow-splash" role="img" aria-label="Rainbow watercolour splash"></div>
    <div class="guinea-pig-art" role="img" aria-label="Illustration of a brown and white guinea pig"></div>
    <div class="beagle-art" role="img" aria-label="Photo of a beagle puppy lying down"></div>
    <h1 class="brand-name">GENTLY BY NATURE</h1>
    <p class="tagline">Cruelty Free Products</p>
    <p class="contact-name">Norma Faldt</p>
    <p class="contact-phone">0492 837 514</p>
  </div>
</body>
</html>
```